Voyage "FUN & RENCONTRES" réservé aux +21
Besoins
Fort de nos compétences, notre agence a été la première à développer les concepts "spring break" en Belgique francophone en réunissant des centaines d'étudiants en Espagne pour faire la fête !
Suite à un souci de santé, notre graphiste habituel ne peut s'occuper de nos réalisations.
Nous recherchons une personne sur le long terme (= si travail sérieux, échanges de coordonnées et autres "contrats").
Il nous faudra également une couverture facebook (cover) et une affiche format A4 recto seul.
Le nom du concept est COASTAL GLOW.
Vous être libre de me créer un beau et nouveau logo bien entendu.
Celui-ci pourra éventuellement être mis sur des futurs t-shirts pour notre staff d'animateurs pendant le voyage ou offert au public !
Voici le travail à effectuer :
- Objectif NOUVEAU CONCEPT 2018 en Bulgarie -
Il nous faut un visuel (flyer efficace et dynamique pour attirer une population entre 21 et 35 ans.
Idée du flyers : format carte postale A6 paysage, vintage, avec un beau visuel au recto qui donne envie et éveille la curiosité (avec titre du voyage "COASTAL GLOW - Bulgarie 2018") et la mention "New Concept" avec notre logo MIRALDO TRAVEL.
Au verso, sur la moitier gauche de la carte postale : petit mot doux d'une femme, du style "Hey ! Le soleil est bien là, les cocktails sont savoureux et l'ambiance incroyable ! On t'attends avec les filles ! Je t'embrasse. Lena" avec un faux baiser (= smack).
Sur la moitier droite, les informations utiles au séjours à savoir :
- du samedi 1 au samedi 8 septembre 2018 (format au choix pour la date)
- Roches Claires, Bulgarie
- Voyage "tout compris" : vol aller-retour, hôtel 4**** formule ALL INCLUSIVE, entrées en boites, cocktails offerts, beach party, ... & bien plus !
- prix : € 599,00 par personne en chambre double
- plus d'infos sur www.coastal-glow-demo.com ou au 0471 820 946
Ci-joint le logo de notre agence + quelques visuels de notre dernier voyage en Hongrie (histoire de vous donner un peu l'effet à ressentir ATTENTION je veux autre chose ici pas du copier coller svp merci)
Bonne chance à tous !
La cible
Public entre 21 et 35 ans - aiment la fête, le soleil et les nouvelles rencontres
Couleurs, favoris et autres exigences:
Couleurs chaudes, festives

```html
<!DOCTYPE html>
<html lang="fr">
<head>
<meta charset="utf-8">
<title>Coastal Glow – Roches Claires, Bulgarie 2018</title>
<link rel="stylesheet" href="https://fonts.googleapis.com/css2?family=Kalam:wght@400&family=Lobster+Two:ital,wght@1,700&family=Open+Sans:wght@400;600;700&family=Oswald:wght@500;600&display=swap">
<style>
  :root {
    --sky-top: #8ce4f1;
    --sky-bottom: #aaeef6;
    --pink: #e8267c;
    --blue: #1f6fd3;
    --bubble: rgba(196, 160, 222, 0.78);
    --white: #ffffff;
    --lip-red: #e0283a;
    --lip-light: #f47c84;
    --sea-deep: #3b8fd8;
    --sea-light: #cfe9fb;
  }
  * { margin: 0; padding: 0; box-sizing: border-box; }
  html, body { width: 1200px; height: 852px; overflow: hidden; }
  body { background: var(--sky-bottom); }

  .postcard {
    position: relative;
    width: 1200px;
    height: 852px;
    overflow: hidden;
    background: linear-gradient(180deg, var(--sky-top) 0%, var(--sky-bottom) 100%);
  }

  /* Left half: message bubble */
  .message-bubble { position: absolute; left: 0; top: 0; width: 560px; height: 740px; }
  .message {
    position: absolute;
    left: 44px; width: 450px;
    text-align: center;
    font-family: "Kalam", cursive;
  }
  .message-hey {
    top: 114px;
    font-size: 34px;
    letter-spacing: 12px;
    color: var(--pink);
  }
  .message-body {
    top: 170px;
    font-size: 28px;
    line-height: 56px;
    color: var(--blue);
  }
  .kiss-mark {
    position: absolute;
    left: 180px; top: 456px;
    width: 184px; height: 124px;
    border-radius: 50%;
    background: radial-gradient(ellipse at 50% 50%, var(--lip-light) 0%, var(--lip-red) 60%, rgba(224, 40, 58, 0) 72%);
  }

  /* Right half: trip information */
  .info { position: absolute; left: 656px; width: 510px; text-align: center; }
  .band {
    background: var(--pink);
    color: var(--white);
    font-family: "Oswald", sans-serif;
    font-weight: 600;
    text-transform: uppercase;
  }
  .band-dates { top: 26px; height: 50px; line-height: 50px; font-size: 23px; letter-spacing: 0.5px; }
  .destination {
    top: 98px;
    font-family: "Lobster Two", cursive;
    font-style: italic;
    font-weight: 700;
    font-size: 38px;
    color: var(--pink);
    white-space: nowrap;
  }
  .detail {
    font-family: "Open Sans", sans-serif;
    font-size: 24px;
    color: var(--blue);
    white-space: nowrap;
  }
  .detail-package { top: 186px; line-height: 36px; }
  .detail-flight { top: 226px; left: 780px; width: auto; text-align: left; line-height: 36px; }
  .plane {
    position: absolute;
    left: 634px; top: 228px;
    width: 136px; height: 34px;
    border-radius: 17px;
    background: linear-gradient(90deg, rgba(255,255,255,0) 0%, #e9eef3 40%, #9aa7b4 100%);
  }
  .hotel {
    top: 274px;
    font-family: "Open Sans", sans-serif;
    font-weight: 700;
    font-size: 27px;
    line-height: 40px;
    color: var(--pink);
  }
  .hotel-stars { font-size: 28px; letter-spacing: 2px; }
  .band-inclusive { top: 326px; height: 46px; line-height: 46px; font-size: 26px; letter-spacing: 1px; }
  .extras { top: 380px; line-height: 40px; }
  .price { top: 476px; line-height: 40px; color: var(--pink); font-weight: 600; }
  .contact { top: 515px; line-height: 50px; color: var(--pink); font-weight: 600; font-size: 23px; }
  .contact-link { font-weight: 700; }

  .shore { position: absolute; left: 0; top: 0; width: 1200px; height: 852px; }
</style>
</head>
<body>
  <main class="postcard">

    <svg class="message-bubble" viewBox="0 0 560 740" aria-hidden="true">
      <path fill="var(--bubble)" d="M82 66 H456 Q494 66 494 104 V604 Q494 642 456 642 H168 L112 712 L124 642 H82 Q44 642 44 604 V104 Q44 66 82 66 Z"/>
    </svg>

    <p class="message message-hey">HEY !</p>
    <p class="message message-body">
      Le soleil est bien là,<br>
      les cocktails sont savoureux<br>
      et l'ambiance incroyable !<br>
      On t'attends avec les filles !<br>
      Je t'embrasse. Lena
    </p>
    <div class="kiss-mark" role="img" aria-label="Trace de baiser au rouge à lèvres"></div>

    <p class="info band band-dates">Samedi 1 au samedi 8 septembre 2018</p>
    <h1 class="info destination">- Roches Claires, Bulgarie -</h1>
    <p class="info detail detail-package">Voyage "tout compris"</p>
    <div class="plane" role="img" aria-label="Avion de ligne en vol"></div>
    <p class="info detail detail-flight">Vol aller-retour</p>
    <p class="info hotel">HÔTEL 4 <span class="hotel-stars">★★★★</span></p>
    <p class="info band band-inclusive">All inclusive</p>
    <p class="info detail extras">
      entrées en boites, cocktails offerts,<br>
      beach party, ... &amp; bien plus !
    </p>
    <p class="info detail price">€ 599,00 par personne en chambre double</p>
    <p class="info detail contact">
      plus d'infos : <span class="contact-link">www.coastal-glow-demo.com</span><br>
      ou au 0471 820 946
    </p>

    <svg class="shore" viewBox="0 0 1200 852" aria-hidden="false">
      <defs>
        <linearGradient id="beachSky" x1="0" y1="0" x2="0" y2="1">
          <stop offset="0" stop-color="var(--sea-light)"/>
          <stop offset="1" stop-color="var(--sea-deep)"/>
        </linearGradient>
      </defs>
      <g role="img" aria-label="Photo de plage : ciel bleu, nuages et palmier">
        <path fill="url(#beachSky)" d="M0 720 C40 716 90 706 170 698 C300 686 440 738 600 754 C720 766 860 732 1000 710 C1080 698 1120 706 1200 721 L1200 852 L0 852 Z"/>
      </g>
      <path fill="var(--white)" d="M0 694 C40 690 90 680 170 672 C300 660 440 712 600 728 C720 740 860 706 1000 684 C1080 672 1120 680 1200 695 L1200 721 C1120 706 1080 698 1000 710 C860 732 720 766 600 754 C440 738 300 686 170 698 C90 706 40 716 0 720 Z"/>
      <path fill="none" stroke="var(--pink)" stroke-width="5" d="M0 694 C40 690 90 680 170 672 C300 660 440 712 600 728 C720 740 860 706 1000 684 C1080 672 1120 680 1200 695"/>
    </svg>

  </main>
</body>
</html>
```